Online-Marketing Material für Immobilienmakler
Zielgruppe
Ich bin Immobilienmakler und beschäftige mich mit der Vermietung / Verkauf von Immobilien. Zielgruppe sind Käufer / Verkäufer bzw. Vermieter und Mieter
Aufgabenstellung
Das Design soll sich am bestehenden CI orientieren, gleichzeitig modern gestaltet werden. Hierbei geht es mir um die Erstellung von Desginvorlagen für Post in Social-Media-Kanälen, welche ich je nach Inhalt entsprechend anpassen kann.
Inbesondere soll es eine Vorlage für die Vorstellung von neuen Objekten geben, welche immer wieder genutzt werden kann und daher die Inhalte in Canva anpassbar sind.

```html
<!DOCTYPE html>
<html lang="de">
<head>
<meta charset="utf-8">
<title>Klarhaus – Social Post</title>
<link href="https://fonts.googleapis.com/css2?family=Red+Hat+Display:wght@400;500;700&display=swap" rel="stylesheet">
<style>
  :root {
    --brand-blue: #0a80c2;
    --brand-green: #83bf41;
    --slate: #4f555c;
    --paper: #ffffff;
    --backdrop: #e9eaec;
  }
  html, body {
    margin: 0;
    padding: 0;
    width: 1200px;
    height: 1117px;
    overflow: hidden;
    background: var(--backdrop);
  }
  .post {
    position: absolute;
    left: 80px;
    top: 38px;
    width: 1040px;
    height: 1040px;
    box-shadow: 0 6px 24px rgba(0,0,0,0.18);
  }
  .post svg { display: block; width: 100%; height: 100%; }
  .post text { font-family: "Red Hat Display", sans-serif; }
  .headline { font-weight: 700; font-size: 52px; fill: var(--paper); }
  .claim { font-weight: 500; font-size: 48px; fill: var(--paper); }
  .brand-name { font-weight: 700; font-size: 92px; fill: var(--brand-blue); }
  .service { font-weight: 500; font-size: 34px; fill: var(--paper); }
  .contact { font-weight: 500; font-size: 34px; fill: var(--paper); }
</style>
</head>
<body>
<div class="post">
  <svg viewBox="0 0 1430 1430" xmlns="http://www.w3.org/2000/svg">
    <defs>
      <linearGradient id="photoTone" x1="0" y1="0" x2="0" y2="1">
        <stop offset="0" stop-color="#b9c3cb"/>
        <stop offset="0.35" stop-color="#6d7a70"/>
        <stop offset="0.7" stop-color="#3e4c3a"/>
        <stop offset="1" stop-color="#2e3a2c"/>
      </linearGradient>
    </defs>

    <!-- header -->
    <rect class="header" x="0" y="0" width="1430" height="224" fill="var(--paper)"/>
    <g class="brand">
      <rect x="95" y="88" width="64" height="64" fill="var(--brand-green)"/>
      <text class="brand-name" x="185" y="152">Klarhaus</text>
    </g>

    <!-- hero photo area -->
    <polygon class="hero-photo" role="img" aria-label="Foto: modernes Einfamilienhaus mit Solardach in der Abenddämmerung, beleuchtete Fenster, Bäume im Hintergrund"
      points="827,74 1430,74 1430,704 0,704 0,284 390,284 444,224 694,224"
      fill="url(#photoTone)"/>
    <polygon class="accent-slate" points="827,74 1297,74 1244,135 774,135" fill="var(--slate)"/>
    <polygon class="accent-blue" points="0,224 444,224 390,284 0,284" fill="var(--brand-blue)"/>

    <!-- message bars -->
    <polygon class="bar-slate" points="0,692 700,692 826,866 0,866" fill="var(--slate)"/>
    <polygon class="bar-blue" points="705,703 1430,703 1430,866 826,866" fill="var(--brand-blue)"/>
    <text class="headline" x="118" y="764">HAUS ÜBER</text>
    <text class="headline" x="118" y="830">KOPF FÜR SIE DA!</text>
    <text class="claim" x="890" y="774">KOMPETENT.</text>
    <text class="claim" x="890" y="825">ZUVERLÄSSIG. FAIR.</text>

    <!-- services -->
    <rect class="services" x="0" y="866" width="1430" height="564" fill="var(--brand-green)"/>
    <line x1="444" y1="905" x2="444" y2="1155" stroke="#72a935" stroke-width="5"/>
    <line x1="986" y1="905" x2="986" y2="1155" stroke="#72a935" stroke-width="5"/>

    <g class="service-item" text-anchor="middle">
      <circle cx="246" cy="968" r="44" fill="none" stroke="var(--paper)" stroke-width="9"/>
      <text class="service" x="246" y="1084">KAUFEN &amp;</text>
      <text class="service" x="246" y="1122">VERKAUFEN</text>
    </g>
    <g class="service-item" text-anchor="middle">
      <circle cx="715" cy="968" r="44" fill="none" stroke="var(--paper)" stroke-width="9"/>
      <text class="service" x="715" y="1084">PARTNER FÜR</text>
      <text class="service" x="715" y="1122">BAUTRÄGER</text>
    </g>
    <g class="service-item" text-anchor="middle">
      <circle cx="1184" cy="968" r="44" fill="none" stroke="var(--paper)" stroke-width="9"/>
      <text class="service" x="1184" y="1084">MIETEN &amp;</text>
      <text class="service" x="1184" y="1122">VERMIETEN</text>
    </g>

    <!-- contact -->
    <polygon class="contact-band" points="167,1215 1291,1215 1262,1291 138,1291" fill="var(--brand-blue)"/>
    <g class="icon-phone">
      <circle cx="284" cy="1252" r="20" fill="var(--paper)"/>
      <path d="M276 1240 l6 0 l3 8 l-4 3 q4 8 10 10 l3 -4 l8 3 l0 6 q-2 4 -8 3 q-18 -5 -22 -23 q0 -6 4 -6z" fill="var(--brand-blue)"/>
    </g>
    <text class="contact" x="325" y="1264">0 7000 / 555 210 0</text>
    <line x1="672" y1="1232" x2="672" y2="1274" stroke="#2b95d1" stroke-width="3"/>
    <g class="icon-mail" fill="none" stroke="var(--paper)" stroke-width="3">
      <rect x="709" y="1238" width="44" height="30"/>
      <polyline points="709,1238 731,1256 753,1238"/>
      <polyline points="709,1268 725,1252"/>
      <polyline points="753,1268 737,1252"/>
    </g>
    <text class="contact" x="782" y="1264">info@klarhaus-immo.de</text>

    <g class="icon-web" fill="none" stroke="var(--paper)" stroke-width="3">
      <circle cx="516" cy="1334" r="19"/>
      <ellipse cx="516" cy="1334" rx="8" ry="19"/>
      <line x1="497" y1="1334" x2="535" y2="1334"/>
      <line x1="501" y1="1323" x2="531" y2="1323"/>
      <line x1="501" y1="1345" x2="531" y2="1345"/>
    </g>
    <text class="contact" x="554" y="1346">www.klarhaus-immo.de</text>
  </svg>
</div>
</body>
</html>
```